Verdant Loop Advisors, LLC

I am looking for a simple, clear layout with my logo prominent and embossed, on the best quality card stock available. I would like the business name and phone number included on the card as well......I dont want my name anywhere on the card and I would like my logo embossed on the card......something simple with a white back......open to designs as long as they go along with recycling symbols and green type stuff.....The address, website, cell number, fax number, and email are listed below

5374 Tillbury Fenwood Road
Larkmont, MD 20999

c. 240.555.0143 f. 240.555.0187
e. sales@verdantloopadvisors.example
w. www.verdantloopadvisors.example

Industry/Entity Type

Recycling

```html
<!DOCTYPE html>
<html lang="en">
<head>
<meta charset="utf-8">
<title>Verdant Loop Advisors, LLC — Business Card</title>
<link rel="stylesheet" href="https://fonts.googleapis.com/css2?family=Open+Sans:wght@400;700&display=swap">
<style>
  :root {
    --backdrop: #3a1516;
    --card: #ffffff;
    --green: #2e7a3a;
    --ink: #1b1b1b;
    --text: #222222;
  }
  * { margin: 0; padding: 0; box-sizing: border-box; }
  html, body {
    width: 1200px;
    height: 800px;
    overflow: hidden;
    background: var(--backdrop);
    font-family: "Open Sans", Arial, sans-serif;
  }
  .business-card {
    position: absolute;
    left: 180px;
    top: 160px;
    width: 840px;
    height: 480px;
    background: var(--card);
    overflow: hidden;
    box-shadow: 0 18px 40px rgba(0,0,0,0.45);
  }
  .accent-panel {
    position: absolute;
    inset: 0;
    width: 840px;
    height: 480px;
  }
  .brand {
    position: absolute;
    left: 48px;
    top: 118px;
    display: flex;
    align-items: center;
    gap: 16px;
  }
  .brand-mark {
    width: 46px;
    height: 46px;
    background: var(--green);
  }
  .brand-name {
    font-weight: 700;
    font-size: 30px;
    letter-spacing: 0.5px;
    color: var(--ink);
    text-transform: uppercase;
  }
  .contact {
    position: absolute;
    left: 48px;
    top: 282px;
    color: var(--text);
    font-size: 18px;
    line-height: 24px;
    font-style: normal;
  }
  .contact-row {
    display: flex;
    align-items: flex-start;
    gap: 8px;
  }
  .contact-row svg {
    width: 18px;
    height: 18px;
    margin-top: 3px;
    flex: none;
    fill: var(--green);
  }
  .address { margin-bottom: 24px; }
  .contact-list { display: flex; flex-direction: column; gap: 2px; }
</style>
</head>
<body>
  <main class="business-card">
    <svg class="accent-panel" viewBox="0 0 840 480" aria-hidden="true">
      <polygon points="640,0 840,0 840,480 700,480" fill="var(--green)"/>
    </svg>

    <header class="brand">
      <div class="brand-mark"></div>
      <h1 class="brand-name">Verdant Loop Advisors, LLC</h1>
    </header>

    <address class="contact">
      <div class="contact-row address">
        <svg viewBox="0 0 20 20"><path d="M10 2 1 10h3v8h5v-5h2v5h5v-8h3z"/></svg>
        <span>5374 Tillbury Fenwood Road<br>Larkmont, MD 20999</span>
      </div>
      <div class="contact-list">
        <div class="contact-row">
          <svg viewBox="0 0 20 20"><rect x="5" y="1" width="10" height="18" rx="2"/><rect x="7" y="3" width="6" height="9" fill="#fff"/></svg>
          <span>(240) 555-0143</span>
        </div>
        <div class="contact-row">
          <svg viewBox="0 0 20 20"><rect x="5" y="2" width="10" height="6"/><rect x="2" y="7" width="16" height="9" rx="2"/><rect x="5" y="13" width="10" height="5" fill="#fff" stroke="var(--green)" stroke-width="1.5"/></svg>
          <span>(240) 555-0187</span>
        </div>
        <div class="contact-row">
          <svg viewBox="0 0 20 20"><rect x="1" y="4" width="18" height="12" rx="1"/><path d="M2 5l8 6 8-6" fill="none" stroke="#fff" stroke-width="1.6"/></svg>
          <span>sales@verdantloopadvisors.example</span>
        </div>
        <div class="contact-row">
          <svg viewBox="0 0 20 20"><circle cx="10" cy="10" r="9"/><path d="M1 10h18M10 1v18M10 1c-5 5-5 13 0 18M10 1c5 5 5 13 0 18" fill="none" stroke="#fff" stroke-width="1.2"/></svg>
          <span>www.verdantloopadvisors.example</span>
        </div>
      </div>
    </address>
  </main>
</body>
</html>
```